Larkfield Advisory Group LLC Business Card Design

I'm looking for a fresh, sharp, clean and current/modern format for my company. This is a start up in the professional services (security/risk management consulting) industry. Catering to C-suite executives as well as senior director types of halcyon 800 companies.

Target Market(s)

Halcyon 800 companies and their C-suite staff with particular focus on VP of Human Resources and Director of Security.

Industry/Entity Type

Business

Font styles to use
Serif

Colors
0455a3
9bcb3c
acd037
3377b5
eaf1f7

Requirements
Must have
• Fresh, sharp, clean and current/modern look and feel.

```html
<!DOCTYPE html>
<html lang="en">
<head>
<meta charset="UTF-8">
<title>Larkfield Advisory Group – Business Card</title>
<link href="https://fonts.googleapis.com/css2?family=Asap+Condensed:wght@700&display=swap" rel="stylesheet">
<style>
  :root {
    --navy: #1f2a5c;
    --green: #74a640;
    --card: #ffffff;
    --backdrop: #e9eaea;
  }
  html, body {
    margin: 0;
    padding: 0;
    width: 1200px;
    height: 1000px;
    overflow: hidden;
    background: var(--backdrop);
  }
  .card {
    position: absolute;
    left: 322px;
    top: 319px;
    width: 586px;
    height: 314px;
    background: var(--card);
    overflow: hidden;
  }
  .card-edge-left {
    position: absolute;
    left: 0;
    top: 0;
    width: 30px;
    height: 314px;
    background: var(--navy);
  }
  .card-edge-left-accent {
    position: absolute;
    left: 30px;
    top: 0;
    width: 12px;
    height: 314px;
    background: var(--green);
  }
  .card-edge-right {
    position: absolute;
    right: 40px;
    top: 0;
    width: 22px;
    height: 314px;
    background: var(--navy);
  }
  .card-edge-right-accent {
    position: absolute;
    right: 68px;
    top: 0;
    width: 6px;
    height: 314px;
    background: var(--green);
  }
  .brand {
    position: absolute;
    left: 160px;
    top: 120px;
    display: flex;
    align-items: center;
    gap: 16px;
  }
  .brand-mark {
    width: 50px;
    height: 50px;
    border-radius: 50%;
    background: var(--navy);
  }
  .brand-name {
    font-family: "Asap Condensed", "Arial Narrow", sans-serif;
    font-weight: 700;
    color: var(--navy);
    line-height: 1;
    text-transform: uppercase;
  }
  .brand-name .line-main {
    display: block;
    font-size: 36px;
    letter-spacing: 0.5px;
  }
  .brand-name .line-sub {
    display: block;
    font-size: 15px;
    letter-spacing: 2.4px;
    margin-top: 4px;
  }
</style>
</head>
<body>
  <div class="card">
    <div class="card-edge-left"></div>
    <div class="card-edge-left-accent"></div>
    <div class="card-edge-right-accent"></div>
    <div class="card-edge-right"></div>
    <div class="brand">
      <div class="brand-mark"></div>
      <div class="brand-name">
        <span class="line-main">Larkfield</span>
        <span class="line-sub">Advisory Group</span>
      </div>
    </div>
  </div>
</body>
</html>
```